Quartz Pivot Business Card Design

I need a 2-sided business card for my computer engineering consulting company. The card is expected to convey a message of cutting edge forward thinking, and boldnes. I would like the card to be memorable and stand-out on a desk. The card should be bold, modern, clean, and highly professional. I am a big fan of watermarks/shadows and other intersting but restrained uses of the logo. The card can be a shape other than the traditional rectangle. Perhaps a rectangle with rounded edges. All I ask is the card be able to fit into a standard wallet. I will supply two logos, one with a red background, and one with a black background. Please feel free to work with both of these logos.
Updates

Hi all, thank you for your submissions. I will post the original vector file later today. Thank you for your patience.

Regards,

Martin

Target Market(s)

Engineering Buyers, Vice Presidents and Directors

Industry/Entity Type

Computer

Requirements
Must have
• 2 sides

```html
<!DOCTYPE html>
<html lang="en">
<head>
<meta charset="utf-8">
<title>Quartz Pivot Works Ltd – Business Card</title>
<link rel="stylesheet" href="https://fonts.googleapis.com/css2?family=Source+Sans+3:wght@400;600&family=Open+Sans:wght@700&display=swap">
<style>
  :root {
    --backdrop: #a8822c;
    --card: #000000;
    --red: #c8222c;
    --grey: #8c8c8c;
    --white: #ffffff;
    --muted: #9a9a9a;
  }
  html, body {
    margin: 0;
    padding: 0;
    width: 1200px;
    height: 686px;
    overflow: hidden;
    background: var(--backdrop);
  }
  .stage {
    position: relative;
    width: 1200px;
    height: 686px;
    font-family: "Source Sans 3", Arial, sans-serif;
  }
  .card {
    position: absolute;
    width: 510px;
    height: 291px;
    background: var(--card);
    border-radius: 14px;
    overflow: hidden;
    color: var(--white);
  }
  .card--front { left: 67px; top: 116px; }
  .card--back { left: 607px; top: 232px; }
  .card__bands {
    position: absolute;
    left: 0;
    top: 0;
    width: 510px;
    height: 291px;
  }
  .card__web {
    position: absolute;
    right: 0;
    width: 220px;
    bottom: 6px;
    text-align: center;
    font-family: "Open Sans", Arial, sans-serif;
    font-weight: 700;
    font-size: 12px;
    letter-spacing: 1.4px;
    color: var(--white);
  }
  .mark {
    position: absolute;
    background: var(--red);
  }
  .wordmark {
    position: absolute;
    left: 0;
    width: 100%;
    text-align: center;
    color: var(--red);
    font-weight: 400;
    line-height: 1;
    white-space: nowrap;
  }
  .tagline {
    position: absolute;
    left: 0;
    width: 100%;
    text-align: center;
    color: var(--muted);
    line-height: 1;
    white-space: nowrap;
  }
  /* front */
  .card--front .mark { left: 216px; top: 24px; width: 60px; height: 66px; }
  .card--front .wordmark { top: 97px; font-size: 23px; }
  .card--front .tagline { top: 121px; font-size: 11px; letter-spacing: 1.5px; }
  .address {
    position: absolute;
    top: 145px;
    width: 100%;
    text-align: center;
    font-size: 13px;
  }
  .divider {
    position: absolute;
    left: 166px;
    top: 177px;
    width: 157px;
    height: 2px;
    background: linear-gradient(90deg, transparent, #e6e6e6 50%, transparent);
  }
  .person {
    position: absolute;
    top: 192px;
    width: 100%;
    text-align: center;
    white-space: nowrap;
  }
  .person__name { color: var(--red); font-weight: 600; font-size: 16px; }
  .person__sep { display: inline-block; width: 1px; height: 13px; background: var(--white); margin: 0 8px 0 10px; vertical-align: -1px; }
  .person__title { color: var(--muted); font-weight: 600; font-size: 13px; }
  .contacts {
    position: absolute;
    top: 215px;
    left: 0;
    width: 100%;
    display: flex;
    justify-content: center;
    gap: 18px;
    font-size: 13.5px;
    white-space: nowrap;
  }
  .contact { display: flex; align-items: center; gap: 2px; }
  .contact svg { width: 11px; height: 11px; fill: var(--red); }
  /* back */
  .card--back .mark { left: 213px; top: 53px; width: 90px; height: 100px; }
  .card--back .wordmark { top: 163px; font-size: 32px; }
  .card--back .tagline { top: 195px; font-size: 15px; letter-spacing: 2.4px; }
</style>
</head>
<body>
<main class="stage">

  <section class="card card--front" aria-label="Front of card">
    <svg class="card__bands" viewBox="0 0 510 291" aria-hidden="true">
      <defs>
        <linearGradient id="redBand" x1="0" y1="0" x2="0" y2="1">
          <stop offset="0" stop-color="#d52a33"/>
          <stop offset="1" stop-color="#a31b23"/>
        </linearGradient>
      </defs>
      <polygon points="0,274 284,274 277,291 0,291" fill="#8c8c8c"/>
      <polygon points="293,262 510,262 510,291 281,291" fill="url(#redBand)"/>
    </svg>
    <div class="mark" aria-hidden="true"></div>
    <div class="wordmark">QUARTZ PIVOT WORKS LTD</div>
    <div class="tagline">ENGINEERED FOR WHAT'S NEXT</div>
    <div class="address">Street name City, State, zip code</div>
    <div class="divider" aria-hidden="true"></div>
    <div class="person">
      <span class="person__name">Martin</span><span class="person__sep" aria-hidden="true"></span><span class="person__title">Title</span>
    </div>
    <div class="contacts">
      <span class="contact">
        <svg viewBox="0 0 24 24" aria-hidden="true"><path d="M6.6 10.8a15 15 0 0 0 6.6 6.6l2.2-2.2a1 1 0 0 1 1-.25 11.4 11.4 0 0 0 3.6.57 1 1 0 0 1 1 1V20a1 1 0 0 1-1 1A17 17 0 0 1 3 4a1 1 0 0 1 1-1h3.5a1 1 0 0 1 1 1c0 1.250.2 2.45.57 3.57a1 1 0 0 1-.25 1z"/></svg>
        123-456-7890
      </span>
      <span class="contact">
        <svg viewBox="0 0 24 24" aria-hidden="true"><path d="M7 2h10v6H7zM3 9h18v9h-4v4H7v-4H3zm6 7v4h6v-4z"/></svg>
        123-456-7890
      </span>
      <span class="contact">
        <svg viewBox="0 0 24 24" aria-hidden="true"><path d="M2 5h20v14H2zm2 2v.5l8 5 8-5V7z"/></svg>
        name@website.com
      </span>
    </div>
    <div class="card__web">www.website.com</div>
  </section>

  <section class="card card--back" aria-label="Back of card">
    <svg class="card__bands" viewBox="0 0 510 291" aria-hidden="true">
      <defs>
        <linearGradient id="redBandBack" x1="0" y1="0" x2="0" y2="1">
          <stop offset="0" stop-color="#d52a33"/>
          <stop offset="1" stop-color="#a31b23"/>
        </linearGradient>
      </defs>
      <polygon points="0,274 284,274 277,291 0,291" fill="#8c8c8c"/>
      <polygon points="293,262 510,262 510,291 281,291" fill="url(#redBandBack)"/>
    </svg>
    <div class="mark" aria-hidden="true"></div>
    <div class="wordmark">QUARTZ PIVOT WORKS LTD</div>
    <div class="tagline">ENGINEERED FOR WHAT'S NEXT</div>
    <div class="card__web">www.website.com</div>
  </section>

</main>
</body>
</html>
```